PowerPoint design MervoSan

We need a PowerPoint set-up based upon our existing logo (see joint file)
Our company is operating in the health care and life science sector. We are mainly focussing on international business

Target Market(s)

International

Industry/Entity Type

health care and life sciences

Requirements
Must have
• Logos as added

```html
<!DOCTYPE html>
<html lang="en">
<head>
<meta charset="utf-8">
<title>MervoSan Presentation Template</title>
<link href="https://fonts.googleapis.com/css2?family=Barlow:wght@700&family=Poppins:ital,wght@0,400;0,500;0,600;0,700;1,500&family=Inter:wght@400;500;600&display=swap" rel="stylesheet">
<style>
:root{
  --page:#f0f1f2;
  --green:#5cbf2a;
  --green-dark:#3f9e22;
  --blue:#1c4b86;
  --navy:#173f6b;
  --bar-navy:#123a6e;
  --bar-green:#4cb61f;
  --bar-purple:#2e1fbf;
  --ink:#222;
  --grey:#555;
  --white:#fff;
}
*{margin:0;padding:0;box-sizing:border-box}
html,body{width:1200px;height:4057px;overflow:hidden;background:var(--page)}
body{position:relative;font-family:"Inter",sans-serif;color:var(--ink)}
.slide{position:absolute;left:68px;width:1064px;height:598px;overflow:hidden;background:var(--white)}
.abs{position:absolute}
.hero{background:linear-gradient(180deg,var(--green) 0%,#3f9a3a 45%,var(--blue) 100%)}
.frame{position:absolute;inset:16px;border:3px solid var(--white)}
.brand-circle{position:absolute;border-radius:50%;border:6px solid var(--white)}
.brand-name{position:absolute;font-family:"Poppins",sans-serif;font-weight:500;color:var(--white);white-space:nowrap;line-height:1}
.hero-title{left:0;right:0;top:305px;text-align:center;font-family:"Barlow",sans-serif;font-weight:700;font-size:46px;color:var(--white)}
.hero-text{left:157px;width:750px;top:364px;text-align:center;font-size:13.5px;line-height:25px;color:var(--white)}
.down{left:514px;top:462px;width:36px;height:36px}
/* agenda */
.agenda-side{left:0;top:0;width:287px;height:598px;background:var(--blue)}
.agenda-photo{left:287px;top:0;width:310px;height:598px;background:linear-gradient(135deg,#e9dcc4 0%,#c8c2b8 40%,#8d96a0 75%,#d9dde2 100%)}
.text-here{left:20px;top:37px;font-family:"Poppins",sans-serif;font-weight:600;font-size:15px;color:var(--white)}
.agenda-rule{left:28px;top:282px;width:55px;height:2px;background:var(--white)}
.agenda-title{left:28px;top:290px;font-family:"Poppins",sans-serif;font-weight:600;font-size:34px;color:var(--white)}
.agenda-list{left:587px;top:0;list-style:none}
.agenda-list li{position:absolute;left:0;display:flex;align-items:center;gap:16px;white-space:nowrap;font-family:"Poppins",sans-serif;font-weight:600;font-size:16.5px;color:var(--ink)}
.agenda-list svg{width:30px;height:30px;flex:none}
/* content slides */
.slide-title{left:27px;top:10px;font-family:"Poppins",sans-serif;font-weight:700;font-size:32px;color:var(--ink)}
.slide-sub{left:27px;top:52px;font-family:"Poppins",sans-serif;font-size:11px;letter-spacing:5px;color:var(--blue);font-weight:500}
.corner-brand{right:24px;top:12px;display:flex;align-items:center;gap:10px}
.corner-brand span.dot{width:48px;height:48px;border-radius:50%;border:4px solid var(--blue)}
.corner-brand span.name{font-family:"Poppins",sans-serif;font-weight:500;font-size:28px;color:var(--blue)}
.band{left:0;top:157px;width:553px;height:48px;background:#efefef}
.band-label{right:40px;top:170px;font-family:"Poppins",sans-serif;font-weight:500;font-size:15px;width:300px;text-align:right;right:auto;left:213px}
.body-text{left:27px;top:224px;width:489px;font-family:"Poppins",sans-serif;font-size:12px;line-height:23.8px;color:var(--grey);text-align:justify}
.lab-photo{left:553px;top:104px;width:487px;height:416px;border-radius:16px;background:linear-gradient(160deg,#5b7fa8 0%,#2b3e5c 50%,#1a2a44 80%,#2d5fd0 100%)}
.footer{left:27px;right:24px;top:578px;display:flex;justify-content:space-between;font-size:8px;color:var(--ink);letter-spacing:.2px}
.footer-line{left:0;bottom:0;width:100%;height:3px;background:var(--green)}
/* quote */
.q-line{height:2px;background:var(--white)}
.q-dot{width:9px;height:9px;border-radius:50%;background:var(--white)}
.q-mark{left:565px;top:249px;width:56px;height:56px;border-radius:50%;background:var(--white);text-align:center;font-family:"Poppins",sans-serif;font-weight:700;font-size:58px;line-height:80px;color:var(--blue)}
.q-text{left:110px;width:844px;top:319px;text-align:center;font-family:"Poppins",sans-serif;font-style:italic;font-weight:500;font-size:17px;line-height:34.5px;color:var(--white)}
.q-author{left:0;right:0;top:434px;text-align:center;font-family:"Poppins",sans-serif;font-weight:500;font-size:17px;color:var(--white)}
/* chart slide */
.chart{left:30px;top:110px;width:500px;height:300px}
.series{left:548px;width:480px;font-family:"Inter",sans-serif}
.series h3{font-size:18.5px;font-weight:500;display:flex;align-items:center;gap:10px;line-height:1}
.series h3::before{content:"";width:7px;height:7px;background:currentColor}
.series p{font-size:15px;line-height:25px;color:var(--grey);margin-left:18px;margin-top:8px}
.s1{color:var(--bar-navy)}.s2{color:var(--bar-green)}.s3{color:var(--bar-purple)}
.chart-head{left:24px;top:440px;font-family:"Inter",sans-serif;font-weight:600;font-size:19px}
.chart-para{left:24px;top:470px;width:1010px;font-size:15px;line-height:29px;color:var(--grey)}
/* thank you */
.contact-band{left:0;top:261px;width:1064px;height:181px;background:var(--navy);display:flex}
.contact{flex:none;display:flex;flex-direction:column;align-items:center;justify-content:flex-start;padding-top:36px;color:var(--white);font-family:"Inter",sans-serif;font-weight:500;font-size:21px;line-height:31px;text-align:center}
.contact svg{width:40px;height:40px;margin-bottom:6px}
.contact+.contact{border-left:1px solid rgba(255,255,255,.45)}
.thanks{left:0;right:0;top:470px;text-align:center;font-family:"Poppins",sans-serif;font-weight:700;font-size:58px;color:var(--white)}
</style>
</head>
<body>

<!-- Title slide -->
<section class="slide hero" style="top:90px" role="img" aria-label="Title slide with a photo of medical staff tinted green and blue">
  <div class="frame"></div>
  <div class="brand-circle" style="left:187px;top:105px;width:170px;height:170px"></div>
  <div class="brand-name" style="left:411px;top:140px;font-size:100px">MervoSan</div>
  <h1 class="abs hero-title">THIS IS YOUR PRESENTATION TITLE</h1>
  <p class="abs hero-text">Lorem ipsum dolor sit amet, consectetur adipiscing elit, sed do eiusmod tempor incididunt ut labore et dolore magna aliqua. Quis ips suspendisse ultrices gravida. Risus commodo viverra maecenas accumsan lacus vel facilisis. Lorem ipsum dolor sit amet, consectetur adipiscing elit, sed do eiusmod</p>
  <svg class="abs down" viewBox="0 0 36 36" fill="none" stroke="#fff" stroke-width="2"><circle cx="18" cy="18" r="16"/><path d="M18 10v15M12 19l6 6 6-6"/></svg>
</section>

<!-- Agenda slide -->
<section class="slide" style="top:742px">
  <div class="abs agenda-side"></div>
  <div class="abs text-here">TEXT HERE</div>
  <div class="abs agenda-rule"></div>
  <h2 class="abs agenda-title">AGENDA</h2>
  <div class="abs" style="left:24px;top:537px;display:flex;align-items:center;gap:12px">
    <span style="width:46px;height:46px;border-radius:50%;border:4px solid #fff;display:block"></span>
    <span style="font-family:Poppins,sans-serif;font-weight:500;font-size:26px;color:#fff">MervoSan</span>
  </div>
  <div class="abs agenda-photo" role="img" aria-label="Photo of a doctor typing on a laptop beside a stethoscope"></div>
  <ul class="abs agenda-list">
    <li style="top:72px"><svg viewBox="0 0 30 30"><circle cx="15" cy="15" r="14" fill="#4cb61f"/><circle cx="15" cy="15" r="8" fill="none" stroke="#fff" stroke-width="1.5"/><path d="M13.5 11.5l3.5 3.5-3.5 3.5" fill="none" stroke="#fff" stroke-width="1.5"/></svg>FINIBUS BONORUM ET MALORUM</li>
    <li style="top:142px"><svg viewBox="0 0 30 30"><circle cx="15" cy="15" r="14" fill="#4cb61f"/><circle cx="15" cy="15" r="8" fill="none" stroke="#fff" stroke-width="1.5"/><path d="M13.5 11.5l3.5 3.5-3.5 3.5" fill="none" stroke="#fff" stroke-width="1.5"/></svg>FINIBUS BONORUM ET MALORUM</li>
    <li style="top:212px"><svg viewBox="0 0 30 30"><circle cx="15" cy="15" r="14" fill="#4cb61f"/><circle cx="15" cy="15" r="8" fill="none" stroke="#fff" stroke-width="1.5"/><path d="M13.5 11.5l3.5 3.5-3.5 3.5" fill="none" stroke="#fff" stroke-width="1.5"/></svg>FINIBUS BONORUM ET MALORUM</li>
    <li style="top:282px"><svg viewBox="0 0 30 30"><circle cx="15" cy="15" r="14" fill="#4cb61f"/><circle cx="15" cy="15" r="8" fill="none" stroke="#fff" stroke-width="1.5"/><path d="M13.5 11.5l3.5 3.5-3.5 3.5" fill="none" stroke="#fff" stroke-width="1.5"/></svg>FINIBUS BONORUM ET MALORUM</li>
    <li style="top:352px"><svg viewBox="0 0 30 30"><circle cx="15" cy="15" r="14" fill="#4cb61f"/><circle cx="15" cy="15" r="8" fill="none" stroke="#fff" stroke-width="1.5"/><path d="M13.5 11.5l3.5 3.5-3.5 3.5" fill="none" stroke="#fff" stroke-width="1.5"/></svg>FINIBUS BONORUM ET MALORUM</li>
    <li style="top:422px"><svg viewBox="0 0 30 30"><circle cx="15" cy="15" r="14" fill="#4cb61f"/><circle cx="15" cy="15" r="8" fill="none" stroke="#fff" stroke-width="1.5"/><path d="M13.5 11.5l3.5 3.5-3.5 3.5" fill="none" stroke="#fff" stroke-width="1.5"/></svg>FINIBUS BONORUM ET MALORUM</li>
    <li style="top:492px"><svg viewBox="0 0 30 30"><circle cx="15" cy="15" r="14" fill="#4cb61f"/><circle cx="15" cy="15" r="8" fill="none" stroke="#fff" stroke-width="1.5"/><path d="M13.5 11.5l3.5 3.5-3.5 3.5" fill="none" stroke="#fff" stroke-width="1.5"/></svg>FINIBUS BONORUM ET MALORUM</li>
  </ul>
</section>

<!-- Content slide -->
<section class="slide" style="top:1394px">
  <h2 class="abs slide-title">Your Title Here</h2>
  <div class="abs slide-sub">SUBTITLE GOES HERE</div>
  <div class="abs corner-brand"><span class="dot"></span><span class="name">MervoSan</span></div>
  <div class="abs band"></div>
  <div class="abs band-label">Content here</div>
  <p class="abs body-text">Lorem ipsum dolor sit amet, consectetur adipiscing elit, sed do eiusmod tempor incididunt ut labore et dolore magna aliqua. Quis ipsum suspee ultrices gravida. Risus commodo viverra maecenas accumsan lacus vel facis. Lorem ipsum dolor sit amet, consectetur adipiscing elit, sed do eiusmod teor incididunt ut labore et dolore magna aliqua. Quis ipsum suspendisse ultrices gravida. Risus commodo viverra maecenas accumsan lacus vel facilim ipsum dolor sit amet, consectetur adipiscing elit, sed do eiusmod tempor inunt ut labore et dolore magna aliqua. Quis ipsum suspendisse ultrices gravi commodo viverra maecenas accumsan lacus vel facilisis. Lorem ipsum dolor sit amet, consectetur adipiscing elit, sed do eiusmod tempor incididunt ut labore et dolore magna aliqua. Quis ipsum suspendisse ultrices gravida.</p>
  <div class="abs lab-photo" role="img" aria-label="Photo of three scientists working with test tubes in a laboratory"></div>
  <div class="abs footer"><span>COPYRIGHT © 2022 – MERVOSAN. ALL RIGHT RESERVED</span><span>PAGE : 03</span></div>
  <div class="abs footer-line"></div>
</section>

<!-- Quote slide -->
<section class="slide hero" style="top:2047px" role="img" aria-label="Quote slide over a tinted photo of laboratory glassware">
  <div class="frame"></div>
  <div class="brand-circle" style="left:310px;top:102px;width:110px;height:110px;border-width:5px"></div>
  <div class="brand-name" style="left:451px;top:122px;font-size:64px">MervoSan</div>
  <div class="abs q-line" style="left:141px;top:276px;width:779px"></div>
  <div class="abs q-dot" style="left:137px;top:272px"></div>
  <div class="abs q-dot" style="left:915px;top:272px"></div>
  <div class="abs q-mark">“</div>
  <p class="abs q-text">Lorem ipsum dolor sit amet, consectetur adipiscing elit, sed do eiusmod tempor incididunt ut labore et dolore magna aliqua. Quis ipsum suspendisse ultrices gravida. Risus commodo viverra maecenas accumsan lacus vel facilisis.</p>
  <div class="abs q-author">- Alan Porter</div>
  <div class="abs q-line" style="left:252px;top:480px;width:559px"></div>
  <div class="abs q-dot" style="left:248px;top:476px"></div>
  <div class="abs q-dot" style="left:806px;top:476px"></div>
</section>

<!-- Chart slide -->
<section class="slide" style="top:2701px">
  <h2 class="abs slide-title" style="left:24px">Your Title Here</h2>
  <div class="abs slide-sub" style="left:24px">SUBTITLE GOES HERE</div>
  <div class="abs corner-brand"><span class="dot"></span><span class="name">MervoSan</span></div>
  <svg class="abs chart" viewBox="0 0 500 300" font-family="Inter,sans-serif" font-size="17" fill="#222">
    <g stroke="#ccc" stroke-width="1">
      <line x1="44" y1="19" x2="485" y2="19"/><line x1="44" y1="58" x2="485" y2="58"/>
      <line x1="44" y1="98" x2="485" y2="98"/><line x1="44" y1="137" x2="485" y2="137"/>
      <line x1="44" y1="176" x2="485" y2="176"/><line x1="44" y1="216" x2="485" y2="216"/>
    </g>
    <line x1="44" y1="255" x2="485" y2="255" stroke="#888"/>
    <line x1="44" y1="19" x2="44" y2="255" stroke="#888"/>
    <g text-anchor="end"><text x="25" y="261">0</text><text x="25" y="222">1</text><text x="25" y="182">2</text><text x="25" y="143">3</text><text x="25" y="104">4</text><text x="25" y="64">5</text><text x="25" y="25">6</text></g>
    <g fill="var(--bar-navy)"><rect x="66" y="86" width="23" height="169"/><rect x="173" y="157" width="23" height="98"/><rect x="282" y="117" width="23" height="138"/><rect x="390" y="78" width="23" height="177"/></g>
    <g fill="var(--bar-green)"><rect x="90" y="157" width="23" height="98"/><rect x="197" y="82" width="23" height="173"/><rect x="306" y="184" width="23" height="71"/><rect x="414" y="145" width="23" height="110"/></g>
    <g fill="var(--bar-purple)"><rect x="114" y="176" width="23" height="79"/><rect x="221" y="176" width="23" height="79"/><rect x="330" y="137" width="23" height="118"/><rect x="438" y="58" width="23" height="197"/></g>
    <g font-size="15"><rect x="98" y="280" width="7" height="7" fill="var(--bar-navy)"/><text x="111" y="288">Series 1</text>
    <rect x="195" y="280" width="7" height="7" fill="var(--bar-green)"/><text x="208" y="288">Series 2</text>
    <rect x="293" y="280" width="7" height="7" fill="var(--bar-purple)"/><text x="306" y="288">Series 3</text></g>
  </svg>
  <div class="abs series" style="top:118px"><h3 class="s1">Series 1</h3><p>Sed ut perspiciatis unde omnis iste natus error sit voluptatem accusantium doloremque laudantium, totam rem aperiam</p></div>
  <div class="abs series" style="top:216px"><h3 class="s2">Series 2</h3><p>Sed ut perspiciatis unde omnis iste natus error sit voluptatem accusantium doloremque laudantium, totam rem aperiam</p></div>
  <div class="abs series" style="top:314px"><h3 class="s3">Series 3</h3><p>Sed ut perspiciatis unde omnis iste natus error sit voluptatem accusantium doloremque laudantium, totam rem aperiam</p></div>
  <h3 class="abs chart-head">The standard Lorem Ipsum passage Finibus Bonorum et Malorum</h3>
  <p class="abs chart-para">Sed ut perspiciatis unde omnis iste natus error sit voluptatem accusantium doloremque laudantium, totam rem aperiam, eaque ipsa quae ab illo inventore veritatis et quasi architecto beatae vitae dicta sunt explicabo.</p>
  <div class="abs footer" style="left:24px"><span>COPYRIGHT © 2022 – MERVOSAN. ALL RIGHT RESERVED</span><span>PAGE : 05</span></div>
  <div class="abs footer-line"></div>
</section>

<!-- Closing slide -->
<section class="slide hero" style="top:3353px" role="img" aria-label="Closing slide over a tinted photo of a laboratory">
  <div class="frame"></div>
  <div class="brand-circle" style="left:187px;top:72px;width:170px;height:170px"></div>
  <div class="brand-name" style="left:411px;top:107px;font-size:100px">MervoSan</div>
  <div class="abs contact-band">
    <div class="contact" style="width:405px">
      <svg viewBox="0 0 40 40"><path d="M20 4c-6.6 0-12 5.2-12 11.6C8 24 20 36 20 36s12-12 12-20.4C32 9.2 26.6 4 20 4z" fill="#fff"/><circle cx="20" cy="15.5" r="4.5" fill="var(--navy)"/></svg>
      <span>48 Harbour Lane Springfield<br>USA 20471</span>
    </div>
    <div class="contact" style="width:288px">
      <svg viewBox="0 0 40 40"><path d="M11 6l5 0 3 8-3.5 2.5c1.8 3.8 4.2 6.2 8 8L26 21l8 3v5c0 2-1.5 3.5-3.5 3.5C18 32 8 22 8 9.5 8 7.5 9 6 11 6z" fill="#fff"/><path d="M24 6a10 10 0 0 1 10 10M24 11a5 5 0 0 1 5 5" fill="none" stroke="#fff" stroke-width="2"/></svg>
      <span>+1 555 010 2040</span>
    </div>
    <div class="contact" style="width:371px">
      <svg viewBox="0 0 40 40"><rect x="5" y="10" width="30" height="21" fill="#fff"/><path d="M5 10l15 12 15-12" fill="none" stroke="var(--navy)" stroke-width="2"/></svg>
      <span>info@mervosan.com</span>
    </div>
  </div>
  <div class="abs thanks">THANK YOU</div>
</section>

</body>
</html>
```